Business Card for Makeup Artist

I need a business card designed for my makeup and hair artistry business which is primarily events and weddings focused. The card needs to be sleek, simple, stylish and appealing to women. I would prefer a white background but open to suggestions also. I also love the marble background look. I have attached some example pics. It needs to be a double sided card with logo and/or design on one side and contact details in the centre of the card on the other side. NO LOGO ON BACK. Examples attached.

Target Market(s)

Females age 14-55

Industry/Entity Type

Business

Contact Information for Business Card

Nora Vint
Principal Makeup Artist
P: 0413 925 214
E: nora@lumirabeauty.com.au
W: www.lumirabeauty.com.au

Requirements
Should not have
• No yellow, green, red or blue in the design.

```html
<!DOCTYPE html>
<html lang="en">
<head>
<meta charset="utf-8">
<title>Lumira Makeup Artistry – Business Card</title>
<link href="https://fonts.googleapis.com/css2?family=Playfair+Display:wght@400;700&family=Montserrat:wght@400;500&display=swap" rel="stylesheet">
<style>
  :root {
    --canvas: #d9d8da;
    --panel: #050406;
    --frame-violet: #6a1c8f;
    --frame-magenta: #a446b8;
    --frame-lilac: #b98bd6;
    --frame-plum: #6e2f96;
    --frame-deep: #571f7e;
    --brand-lilac: #a765b6;
    --brand-plum: #9a4ea9;
    --name-pink: #d88ac9;
    --detail-light: #e9dfec;
    --detail-soft: #bda6c8;
  }
  * { margin: 0; padding: 0; box-sizing: border-box; }
  html, body { width: 1200px; height: 1200px; overflow: hidden; }
  body {
    background: var(--canvas);
    display: flex;
    flex-direction: column;
    align-items: center;
    justify-content: center;
    gap: 64px;
    font-family: "Montserrat", Arial, sans-serif;
  }
  .card {
    position: relative;
    width: 900px;
    height: 514px;
    overflow: hidden;
    box-shadow: 0 10px 28px rgba(0,0,0,0.28);
  }
  .card__pattern {
    position: absolute;
    inset: 0;
    background:
      linear-gradient(160deg, rgba(255,255,255,0.10), rgba(0,0,0,0.18)),
      linear-gradient(100deg, var(--frame-violet) 0%, var(--frame-magenta) 30%, var(--frame-lilac) 58%, var(--frame-plum) 82%, var(--frame-deep) 100%);
  }
  .card__panel {
    position: absolute;
    left: 20%;
    right: 0;
    top: 17%;
    bottom: 17%;
    background: var(--panel);
    display: flex;
    flex-direction: column;
    justify-content: center;
    align-items: center;
    text-align: center;
  }
  .brand__name {
    font-family: "Montserrat", Arial, sans-serif;
    font-weight: 500;
    font-size: 104px;
    line-height: 1;
    color: var(--brand-lilac);
    letter-spacing: 2px;
  }
  .brand__tagline {
    margin-top: 8px;
    font-weight: 400;
    font-size: 34px;
    letter-spacing: 3px;
    color: var(--brand-plum);
  }
  .contact__name {
    font-family: "Playfair Display", Georgia, serif;
    font-weight: 700;
    font-size: 68px;
    line-height: 1;
    color: var(--name-pink);
  }
  .contact__role {
    margin-top: 10px;
    font-size: 22px;
    letter-spacing: 2px;
    color: var(--detail-soft);
  }
  .contact__list {
    list-style: none;
    margin-top: 26px;
    font-size: 21px;
    line-height: 1.6;
    color: var(--detail-light);
  }
  .contact__label {
    color: var(--name-pink);
    font-weight: 500;
    margin-right: 8px;
  }
</style>
</head>
<body>

  <section class="card card--front" aria-label="Business card front">
    <div class="card__pattern" role="img" aria-label="Faceted pyramid texture in violet to plum gradient with sparkles"></div>
    <div class="card__panel brand">
      <div class="brand__name">Lumira</div>
      <div class="brand__tagline">MAKEUP ARTISTRY</div>
    </div>
  </section>

  <section class="card card--back" aria-label="Business card back">
    <div class="card__pattern" role="img" aria-label="Faceted pyramid texture in violet to plum gradient with sparkles"></div>
    <div class="card__panel contact">
      <div class="contact__name">Nora Vint</div>
      <div class="contact__role">Principal Makeup Artist</div>
      <ul class="contact__list">
        <li><span class="contact__label">P:</span>0413 925 214</li>
        <li><span class="contact__label">E:</span>nora@lumirabeauty.com.au</li>
        <li><span class="contact__label">W:</span>www.lumirabeauty.com.au</li>
      </ul>
    </div>
  </section>

</body>
</html>
```